TopMoneyswitch.net Mobile App

Topmoneyswitch.net is an online Beurea de change. They buy and sell currency from individuals and large corporations.

The app will compliment the main website of the company and focus on specific features as set out in our brief document. overall the design must be high-quality, easy navigate with a one finger operation and nice clean design.

This content is for the design of 3 screen

Loading screen
Homepage screen
Buy Currency for Branch Collection screen

attached is a full brief, but the loading screen will incorporate the logo and the home screen must allow easy navigation to 6 key button features that will enable you to go to each section of the app.

The winner will get to design the remaining screens of the app which are approx 15/18 further screens, based on the same layout.

If you can code the app as well into iPhone and Android, please make this known as well.
Updates

Hello,

For further inspritation for the Home screen, we quite like the interface on the uploaded image vellorin-home.jpg

So you slide left and right with your finger to the button, instead of a list format or something quite 2d. Almost 3d like interface maybe with an option to display all as a list?

See what sort of creativity can be achieved.

thanks

Target Market(s)

Consumers mainly aged between 25-60

Industry/Entity Type

It Company

Requirements
Must have
• good clean visually stunning appearance with apply shiny effect buttons and navigation

```html
<!DOCTYPE html>
<html lang="en">
<head>
<meta charset="utf-8">
<title>TopMoneyswitch.net – Fast Track Branch Collection</title>
<link href="https://fonts.googleapis.com/css2?family=Source+Sans+3:wght@300;400;600;700&display=swap" rel="stylesheet">
<style>
  :root {
    --brand-red: #d8222a;
    --brand-blue: #1b4f8f;
    --panel-blue: rgba(18, 88, 160, 0.96);
    --panel-edge: #0f4f93;
    --ink: #111;
    --muted: #b9bcc2;
    --paper: #ffffff;
    --band: #1d4e8a;
  }
  * { box-sizing: border-box; margin: 0; padding: 0; }
  html, body { width: 676px; height: 1200px; overflow: hidden; }
  body {
    position: relative;
    background: var(--paper);
    font-family: "Source Sans 3", sans-serif;
    color: var(--ink);
  }
  .top-band {
    position: absolute; left: 0; top: 0; width: 676px; height: 16px;
    background: radial-gradient(circle, #3f6fa8 1px, var(--band) 1.5px) 0 0 / 4px 4px;
  }
  .deco-arrow {
    position: absolute; left: 400px; top: 20px; width: 276px; height: 260px;
    background: linear-gradient(225deg, rgba(216,34,42,0.22), rgba(216,34,42,0.04) 60%, transparent);
  }
  .brand {
    position: absolute; left: 0; top: 48px; width: 676px; text-align: center;
  }
  .brand-name {
    font-size: 62px; font-weight: 600; color: var(--brand-blue); letter-spacing: -1px; line-height: 1;
  }
  .brand-tag {
    margin-top: 14px; font-size: 19px; font-weight: 400; color: #333; letter-spacing: 1px;
  }
  .clock-badge { position: absolute; left: 46px; top: 216px; width: 148px; height: 148px; }
  .page-title {
    position: absolute; left: 190px; top: 238px; width: 420px; text-align: center;
    font-size: 38px; font-weight: 400; line-height: 44px; letter-spacing: 0.5px; color: #000;
  }
  .order-form {
    position: absolute; left: 132px; top: 440px; width: 470px; color: var(--muted);
    font-size: 20px;
  }
  .order-form .site { position: absolute; left: 22px; top: 36px; font-size: 26px; letter-spacing: 1px; }
  .order-form .select { position: absolute; left: 22px; top: 80px; width: 400px; height: 44px; border: 1px solid #ddd; border-radius: 6px; padding: 8px 20px; }
  .order-form .btn { position: absolute; left: 100px; top: 342px; width: 200px; height: 50px; border-radius: 25px; background: #cfd8e3; }
  .terms { position: absolute; left: 96px; top: 884px; font-size: 20px; color: var(--muted); }
  .terms u { text-decoration: underline; }
  .side-tab {
    position: absolute; left: -40px; top: 536px; width: 88px; height: 164px;
    border-radius: 0 82px 82px 0; background: linear-gradient(90deg, #0d3d78, #1f5ea8);
  }
  .side-tab svg { position: absolute; left: 50px; top: 66px; }
  .scene-art {
    position: absolute; left: 90px; top: 966px; width: 520px; height: 234px;
    background: linear-gradient(180deg, #eef0f3 0%, #d9dde2 35%, #d8262e 60%, #b31a21 100%);
    opacity: 0.9;
  }
  .info-panel {
    position: absolute; left: 82px; top: 314px; width: 566px; height: 652px;
    background: var(--panel-blue); border-radius: 20px; color: #fff;
    padding: 26px 30px 0 44px; box-shadow: 0 2px 10px rgba(0,0,0,0.25);
  }
  .info-panel p { font-size: 18.5px; line-height: 27px; }
  .steps { list-style: none; margin-top: 20px; }
  .step { display: flex; margin-bottom: 14px; }
  .step-num {
    width: 40px; flex: none; font-size: 38px; font-weight: 600; line-height: 40px;
    text-decoration: underline; text-underline-offset: 6px; text-decoration-thickness: 2px;
  }
  .step p { padding-left: 0; }
  .note { margin-top: 22px; margin-left: -2px; }
  .note strong { display: block; font-size: 18.5px; font-weight: 700; }
  .close-btn {
    position: absolute; right: 44px; bottom: 28px; display: flex; align-items: center; gap: 6px;
    font-size: 26px; font-weight: 700; letter-spacing: 0.5px;
  }
  .help-btn { position: absolute; left: 592px; top: 284px; }
</style>
</head>
<body>
  <div class="top-band"></div>
  <div class="deco-arrow" role="img" aria-label="Faint rising red arrow decoration"></div>

  <header class="brand">
    <div class="brand-name">topmoneyswitch</div>
    <div class="brand-tag">CURRENCY SPECIALISTS</div>
  </header>

  <svg class="clock-badge" viewBox="0 0 148 148" aria-hidden="true">
    <defs>
      <linearGradient id="ring" x1="0" y1="0" x2="0" y2="1"><stop offset="0" stop-color="#f4f4f4"/><stop offset="1" stop-color="#8d8d8d"/></linearGradient>
      <radialGradient id="ruby" cx="0.45" cy="0.35" r="0.7"><stop offset="0" stop-color="#e8343b"/><stop offset="1" stop-color="#7d0a0f"/></radialGradient>
    </defs>
    <circle cx="74" cy="74" r="72" fill="url(#ring)"/>
    <circle cx="74" cy="74" r="60" fill="url(#ruby)"/>
    <circle cx="74" cy="70" r="28" fill="#fff" stroke="#8a0d12" stroke-width="2"/>
    <path d="M74 50v20l14 8" stroke="#7d0a0f" stroke-width="3" fill="none" stroke-linecap="round"/>
  </svg>

  <h1 class="page-title">FAST TRACK<br>BRANCH COLLECTION</h1>

  <div class="order-form" aria-hidden="true">
    <div class="site">TOPMONEYSWITCH.NET</div>
    <div class="select">Select Currency</div>
    <div class="btn"></div>
  </div>
  <div class="terms">Please ensure that you read our <u>Terms and Conditions</u>.</div>

  <div class="side-tab">
    <svg width="24" height="32" viewBox="0 0 24 32"><path d="M18 4L6 16l12 12" stroke="#fff" stroke-width="4" fill="none" stroke-linecap="round"/></svg>
  </div>

  <div class="scene-art" role="img" aria-label="Illustration of open red gift boxes with currency symbols and a world map"></div>

  <section class="info-panel">
    <p>We can prepare your order in advance for Fast Track Service and collection at any nominated Branch. Just simply complete the order form below and it will be ready for collection with immediate effect.</p>
    <ol class="steps">
      <li class="step"><span class="step-num">1</span><p>Please note that if you are paying by cash or debit card there is no charge from us.</p></li>
      <li class="step"><span class="step-num">2</span><p>Kindly click customer notification for payment terms and necessary supporting documents.</p></li>
      <li class="step"><span class="step-num">3</span><p>To enjoy the preferential on-line rates advertised on this website, you have to place a Fast Track Branch Collection order, otherwise the rates advertised at the branches will apply, which may be adverse to you.</p></li>
    </ol>
    <div class="note">
      <strong>Note:</strong>
      <p>Please be advised that we are governed by the Data Protection Act 1998, as such the confidentiality of your supporting documents are assure</p>
    </div>
    <div class="close-btn">
      <svg width="26" height="26" viewBox="0 0 26 26"><circle cx="13" cy="13" r="11" fill="#111" stroke="#fff" stroke-width="2"/><path d="M9 9l8 8M17 9l-8 8" stroke="#fff" stroke-width="2.5" stroke-linecap="round"/></svg>
      CLOSE
    </div>
  </section>

  <svg class="help-btn" width="52" height="52" viewBox="0 0 52 52" aria-label="Help">
    <circle cx="26" cy="26" r="25" fill="var(--panel-edge)"/>
    <circle cx="26" cy="26" r="15" fill="#fff"/>
    <text x="26" y="33" text-anchor="middle" font-family="Source Sans 3, sans-serif" font-weight="700" font-size="21" fill="#0f4f93">?</text>
  </svg>
</body>
</html>
```